Redesign Talent Management graphic

Need a new, fresh design approach to this graphic. Need it to be sized to fit into a widescreen PPT: 13.33in wide x 7.5in high. Looking for something clean and modern that will still get the message across that we offer products for every stage of the employment lifecycle.

Our brand color palette is red, gray, white, black. The red is PMS 186, or RGB 224, 0, 26.

Font styles to use
Sans Serif

```html
<!DOCTYPE html>
<html lang="en">
<head>
<meta charset="utf-8">
<title>Talent Management Tools – Employee Life Cycle</title>
<link href="https://fonts.googleapis.com/css2?family=Open+Sans:wght@700;800&display=swap" rel="stylesheet">
<style>
  :root {
    --bg: #f4f4f4;
    --glow: #ffffff;
    --brand-red: #e0001a;
    --black: #141414;
    --step-1: #4d4d4d;
    --step-2: #878787;
    --step-3: #a5a5a5;
    --step-4: #bdbdbd;
    --step-5: #d9d9d9;
    --label-dark: #4a4a4a;
    --label-light: #efefef;
    --white: #ffffff;
    --figure-tint: #fbdbe2;
  }
  html, body {
    margin: 0;
    padding: 0;
    width: 1200px;
    height: 1000px;
    overflow: hidden;
    background: var(--bg);
  }
  .canvas {
    position: relative;
    width: 1200px;
    height: 1000px;
    background: radial-gradient(ellipse 520px 420px at 560px 520px, var(--glow) 0%, var(--bg) 100%);
    font-family: "Open Sans", Arial, sans-serif;
  }
  .lifecycle {
    position: absolute;
    inset: 0;
    width: 1200px;
    height: 1000px;
  }
  .label {
    font-family: "Open Sans", Arial, sans-serif;
    font-weight: 700;
    text-transform: uppercase;
    dominant-baseline: central;
  }
  .label--entry { fill: var(--white); font-size: 21px; }
  .label--onboarding { fill: var(--label-light); font-size: 20px; }
  .label--development { fill: var(--label-dark); font-size: 16.5px; }
  .label--potential { fill: var(--label-dark); font-size: 19px; }
  .label--succession { fill: var(--label-dark); font-size: 20px; }
  .label--business { fill: var(--brand-red); font-size: 40px; font-weight: 800; }
  .label--tools { fill: var(--white); font-size: 33px; font-weight: 800; }
  .label--tools-sub { fill: var(--white); font-size: 16.5px; }
  .step--1 { fill: var(--step-1); }
  .step--2 { fill: var(--step-2); }
  .step--3 { fill: var(--step-3); }
  .step--4 { fill: var(--step-4); }
  .step--5 { fill: var(--step-5); }
  .step--tools { fill: var(--brand-red); }
  .entry-arrow { fill: var(--black); }
  .team-figures { fill: var(--figure-tint); }
</style>
</head>
<body>
<main class="canvas">
  <svg class="lifecycle" viewBox="0 0 1200 1000" xmlns="http://www.w3.org/2000/svg">
    <!-- team figures placeholder -->
    <rect class="team-figures" x="895" y="178" width="275" height="622" rx="60"
          role="img" aria-label="Silhouettes of two business professionals standing side by side"/>

    <!-- entry arrow -->
    <polygon class="entry-arrow" points="33,700 230,700 230,690 260,740 230,790 230,780 33,780"/>
    <text class="label label--entry" x="140" y="727" text-anchor="middle">Recruitment</text>
    <text class="label label--entry" x="132" y="757" text-anchor="middle">and Hiring</text>

    <!-- steps -->
    <polygon class="step step--1" points="268,795 268,600 262,600 310,570 357,600 352,600 352,795"/>
    <polygon class="step step--2" points="352,795 352,560 343,560 404,523 465,560 456,560 456,795"/>
    <polygon class="step step--3" points="456,795 456,490 427,490 487,443 548,490 540,490 540,795"/>
    <polygon class="step step--4" points="540,795 540,420 506,420 570,363 633,420 626,420 626,795"/>
    <polygon class="step step--5" points="626,795 626,340 603,340 675,275 746,340 738,340 738,795"/>
    <polygon class="step step--tools" points="738,795 738,245 711,245 810,143 910,245 890,245 890,795"/>

    <!-- step labels (read bottom to top) -->
    <text class="label label--onboarding" transform="translate(310,775) rotate(-90)">On - B- oarding</text>

    <g class="label label--development">
      <text class="label label--development" transform="translate(379,775) rotate(-90)">Employee &amp;</text>
      <text class="label label--development" transform="translate(406,775) rotate(-90)">Leadership</text>
      <text class="label label--development" transform="translate(433,775) rotate(-90)">Development</text>
    </g>

    <text class="label label--potential" transform="translate(483,775) rotate(-90)">High Potential</text>
    <text class="label label--potential" transform="translate(514,775) rotate(-90)">Programs</text>

    <text class="label label--succession" transform="translate(577,775) rotate(-90)">Succession Planning</text>

    <text class="label label--business" transform="translate(677,765) rotate(-90)">Bussiness</text>

    <text class="label label--tools" transform="translate(802,762) rotate(-90)">Talent Management Tools</text>
    <text class="label label--tools-sub" transform="translate(838,690) rotate(-90)">For the life cycle of the employee</text>
  </svg>
</main>
</body>
</html>
```